Lorna's Henna Party Invitation on March 20, 2026

I'd like to design an invitation that would be sent via text and posted on social media for my niece's henna party. The color scheme would be white, gold, and black. I want it to be elegant and classy. The font could be something like Rastanty Cortez. The party would be on March 20, 2026. It's a traditional and cultural type of party (pre-wedding party). I've attached some ideas for inspiration and to get a feel of a henna party.

Target Market(s)

This invitation would only be sent via text to our guests and posted on social media.

Font styles to use
Decorative
Script
Other font styles liked:
• Rastanty Cortez

Requirements
Must have
• Elegance, classy, a henna party reflection but something elegant and perhaps abstract.
Nice to have
• Something reflecting the henna party tradition. It could be a high gold candle, a decorated tray, etc. But I want it to be elegant and less crowded of an invitation.

```html
<!DOCTYPE html>
<html lang="en">
<head>
<meta charset="UTF-8">
<title>Lorna's Henna Party Invitation</title>
<link href="https://fonts.googleapis.com/css2?family=Fira+Mono&family=Jura:wght@300&family=Mrs+Saint+Delafield&display=swap" rel="stylesheet">
<style>
  :root {
    --paper: #ffffff;
    --ink: #111111;
    --gold-deep: #c98f2e;
    --gold-mid: #ddb062;
    --gold-pale: #f3dcaa;
    --gold-whisper: rgba(221, 176, 98, 0.16);
  }
  * { margin: 0; padding: 0; box-sizing: border-box; }
  html, body { width: 858px; height: 1200px; overflow: hidden; background: var(--paper); }
  .invitation {
    position: relative;
    width: 858px;
    height: 1200px;
    background: var(--paper);
    overflow: hidden;
    color: var(--ink);
  }
  .ornament { position: absolute; }
  .ornament--mandala-top {
    left: 540px; top: 0; width: 318px; height: 469px;
    background: radial-gradient(ellipse at 84% 38%, rgba(201,143,46,0.30) 0%, rgba(221,176,98,0.20) 40%, rgba(243,220,170,0.08) 70%, rgba(255,255,255,0) 80%);
  }
  .ornament--mandala-bottom {
    left: 0; top: 692px; width: 306px; height: 508px;
    background: radial-gradient(ellipse at 8% 60%, rgba(201,143,46,0.30) 0%, rgba(221,176,98,0.20) 40%, rgba(243,220,170,0.08) 70%, rgba(255,255,255,0) 80%);
  }
  .ornament--paisley-top {
    left: 66px; top: 57px; width: 314px; height: 475px;
    background: radial-gradient(ellipse at 55% 60%, rgba(243,220,170,0.35) 0%, rgba(243,220,170,0.12) 55%, rgba(255,255,255,0) 75%);
  }
  .ornament--paisley-bottom {
    left: 506px; top: 646px; width: 295px; height: 441px;
    background: radial-gradient(ellipse at 50% 55%, rgba(243,220,170,0.35) 0%, rgba(243,220,170,0.12) 55%, rgba(255,255,255,0) 75%);
  }
  .frame { position: absolute; left: 0; top: 0; }

  .mono { font-family: "Fira Mono", monospace; }
  .intro {
    position: absolute; left: 0; width: 858px; top: 238px;
    padding-left: 209px;
    font-size: 24px; letter-spacing: 2.6px; line-height: 1;
  }
  .title {
    position: absolute;
    font-family: "Mrs Saint Delafield", cursive;
    font-weight: 400; line-height: 1; white-space: nowrap;
  }
  .title--name { left: 300px; top: 352px; font-size: 168px; }
  .title--event { left: 112px; top: 478px; font-size: 168px; }

  .centered {
    position: absolute; left: 230px; width: 620px; text-align: center;
  }
  .quote { top: 772px; font-size: 21px; letter-spacing: 2px; line-height: 39px; }
  .date {
    position: absolute; top: 893px; left: 386px; height: 64px;
    display: flex; align-items: center;
    font-family: "Jura", sans-serif; font-weight: 300;
    font-size: 62px; letter-spacing: 0; line-height: 1;
  }
  .date__part { padding: 0 6px; }
  .date__divider { width: 1px; height: 64px; background: var(--ink); }
  .venue-label { top: 991px; font-size: 21px; letter-spacing: 2px; }
  .venue-name { top: 1025px; font-size: 21px; letter-spacing: 2.4px; }
  .rsvp { top: 1097px; font-size: 21px; letter-spacing: 2.4px; }
</style>
</head>
<body>
<main class="invitation">
  <div class="ornament ornament--paisley-top" role="img" aria-label="Soft gold paisley henna motif with swirls, leaves and dots"></div>
  <div class="ornament ornament--mandala-top" role="img" aria-label="Gold line mandala flower in the upper right corner"></div>
  <div class="ornament ornament--paisley-bottom" role="img" aria-label="Soft gold paisley henna motif with swirls, leaves and dots"></div>
  <div class="ornament ornament--mandala-bottom" role="img" aria-label="Gold line mandala flower in the lower left corner"></div>

  <svg class="frame" width="858" height="1200" viewBox="0 0 858 1200" aria-hidden="true">
    <defs>
      <linearGradient id="goldTop" x1="0" y1="0" x2="1" y2="0">
        <stop offset="0" stop-color="#d29a3c"/>
        <stop offset="1" stop-color="#efd19a"/>
      </linearGradient>
      <linearGradient id="goldLeft" x1="0" y1="0" x2="0" y2="1">
        <stop offset="0" stop-color="#d29a3c"/>
        <stop offset="1" stop-color="#f6e4c0"/>
      </linearGradient>
      <linearGradient id="goldRight" x1="0" y1="0" x2="0" y2="1">
        <stop offset="0" stop-color="#f6e4c0"/>
        <stop offset="1" stop-color="#d29a3c"/>
      </linearGradient>
      <linearGradient id="goldBottom" x1="0" y1="0" x2="1" y2="0">
        <stop offset="0" stop-color="#efd19a"/>
        <stop offset="1" stop-color="#d29a3c"/>
      </linearGradient>
    </defs>
    <line x1="54" y1="45" x2="568" y2="45" stroke="url(#goldTop)" stroke-width="2"/>
    <line x1="54" y1="44" x2="54" y2="704" stroke="url(#goldLeft)" stroke-width="2"/>
    <line x1="818" y1="498" x2="818" y2="1159" stroke="url(#goldRight)" stroke-width="2"/>
    <line x1="305" y1="1158" x2="819" y2="1158" stroke="url(#goldBottom)" stroke-width="2"/>
  </svg>

  <p class="intro mono">Please join us for a</p>

  <h1>
    <span class="title title--name">Lorna's</span>
    <span class="title title--event">Henna Party</span>
  </h1>

  <p class="centered quote mono">“Let's celebrate our beautiful<br>bride to be”</p>

  <p class="date" aria-label="20 March 2026">
    <span class="date__part">20</span>
    <span class="date__divider"></span>
    <span class="date__part">03</span>
    <span class="date__divider"></span>
    <span class="date__part">2026</span>
  </p>

  <p class="centered venue-label mono">Venue</p>
  <p class="centered venue-name mono">Mira Al Saadi’s Residence</p>
  <p class="centered rsvp mono">RSVP : Dana R. Karim</p>
</main>
</body>
</html>
```